earthmoving and roadworks company looking for a fresh and updated logo to help us stand out

We are looking for a business card design for our earthmoving, demolition and road works company named Wombridge Hire. We cover a broad range of work so our business card needs to be flexible to suit all of the different services we provide. We have a few different bits of machinery including several water trucks for transporting water and spraying the roads, an excavator (digger) for earthmoving, a tipper truck that carries grain/soil and other items, a skidmule and two rollers. our business card needs to be simple but effective and bold. Our colour palette is yellow, black and white and I have attached a copy of our logo but please note our logo is only the 'Wombridge hire' bit with attached circle, the 'watercarts, rollers, cartage' below are not part of the logo. Please feel free to modify the logo to better suit the business card. The design must be easy to read and to the point. It should make us look reliable and professional.

Target Market(s)

Wide range of clients including government sectors and private individuals

Industry/Entity Type

Construction

Contact Information for Business Card

We need a business card that is bold and straight to the point but with easy to read information and an eye catching design. We are open to either a single sided or double sided design

Colors
fbee3d
fcf5b5
fbf289
fbed22

Requirements
Must have
• The business card must include
• our logo
• our contact details as listed below:
• Dwayne Ostler
• Managing Director
• 02 6911 5033
• 0477 301 926
• wombridgehire@tallnetmail.com
Nice to have
• Nice to have a picture of machinery or part of machinery in the business card design. We would also like to incorporate our business activities which are: demolition, earthmoving, road works and cartage. It would also be highly desirable if it included a list of our machinery: Watercarts, Rollers, Excavator, Skidmule, Truck & Dog. we are open to the possibility of either single sided or double sided designs
Should not have
• should not have too many colours or detract from the main information. should not be too busy.

```html
<!DOCTYPE html>
<html lang="en">
<head>
<meta charset="utf-8">
<title>Wombridge Hire – Business Card</title>
<link rel="stylesheet" href="https://fonts.googleapis.com/css2?family=Lato:wght@400;700;900&display=swap">
<style>
  :root {
    --yellow: #fbed22;
    --yellow-soft: #fbee3d;
    --black: #161616;
    --ink: #1d1d1d;
    --white: #ffffff;
    --backdrop: #e4e4e4;
    --photo-light: #b9afa6;
    --photo-mid: #8a8078;
    --photo-dark: #4a433e;
  }
  * { box-sizing: border-box; margin: 0; padding: 0; }
  html, body { width: 1200px; height: 926px; overflow: hidden; }
  body {
    background: var(--backdrop);
    font-family: "Lato", Arial, sans-serif;
    color: var(--ink);
    position: relative;
  }
  .card {
    position: absolute;
    width: 720px;
    height: 412px;
    left: 240px;
    background: var(--white);
    box-shadow: 0 6px 18px rgba(0,0,0,0.18);
    overflow: hidden;
  }
  .card--front { top: 34px; }
  .card--back { top: 480px; }

  /* Front */
  .machinery-photo {
    position: absolute;
    inset: 0 0 78px 0;
    background: linear-gradient(160deg, var(--photo-light) 0%, var(--photo-mid) 45%, var(--photo-dark) 100%);
  }
  .front-brand {
    position: absolute;
    left: 360px;
    top: 130px;
    display: flex;
    align-items: center;
    gap: 14px;
  }
  .brand-dot {
    width: 34px; height: 34px;
    border-radius: 50%;
    background: var(--yellow);
    flex: none;
  }
  .front-brand .brand-name {
    font-weight: 900;
    font-size: 34px;
    color: var(--white);
    letter-spacing: 0.5px;
  }
  .service-band {
    position: absolute;
    left: 0; right: 0; bottom: 0;
    height: 78px;
    padding: 0 24px;
    background: var(--black);
    display: flex;
    align-items: center;
    justify-content: center;
  }
  .service-list {
    color: var(--white);
    font-weight: 900;
    font-size: 17px;
    letter-spacing: 1.8px;
    text-transform: uppercase;
    white-space: nowrap;
  }

  /* Back */
  .back-brand {
    position: absolute;
    left: 38px;
    top: 40px;
    display: flex;
    align-items: center;
    gap: 12px;
  }
  .back-brand .brand-dot { width: 28px; height: 28px; }
  .back-brand .brand-name {
    font-weight: 900;
    font-size: 28px;
    color: var(--black);
  }
  .person {
    position: absolute;
    left: 38px;
    top: 262px;
  }
  .person-name {
    font-size: 32px;
    font-weight: 400;
    letter-spacing: 1px;
    text-transform: uppercase;
    color: var(--black);
    line-height: 1;
  }
  .person-name strong { font-weight: 700; }
  .person-role {
    margin-top: 4px;
    font-size: 16px;
    font-weight: 700;
    letter-spacing: 1px;
    text-transform: uppercase;
    color: var(--yellow);
  }
  .contact-list {
    position: absolute;
    left: 380px;
    top: 300px;
    list-style: none;
    font-size: 18px;
    letter-spacing: 0.4px;
    color: var(--black);
  }
  .contact-list li {
    display: flex;
    align-items: center;
    gap: 12px;
    line-height: 26px;
    white-space: nowrap;
  }
  .contact-icon { width: 16px; height: 16px; flex: none; }
  .accent-stripe {
    position: absolute;
    left: 0; right: 0;
    bottom: 8px;
    height: 14px;
    background: var(--yellow);
  }
</style>
</head>
<body>

  <section class="card card--front" aria-label="Business card front">
    <div class="machinery-photo" role="img" aria-label="Photograph of earthmoving machinery on a worksite: excavator, loader and roller in sepia tones"></div>
    <div class="front-brand">
      <span class="brand-dot"></span>
      <span class="brand-name">Wombridge Hire</span>
    </div>
    <div class="service-band">
      <p class="service-list">Watercarts, Rollers, Excavator, Skidmule, Truck &amp; Dog</p>
    </div>
  </section>

  <section class="card card--back" aria-label="Business card back">
    <div class="back-brand">
      <span class="brand-dot"></span>
      <span class="brand-name">Wombridge Hire</span>
    </div>

    <div class="person">
      <p class="person-name">Dwayne <strong>Ostler</strong></p>
      <p class="person-role">Managing Director</p>
    </div>

    <ul class="contact-list">
      <li>
        <svg class="contact-icon" viewBox="0 0 16 16" aria-hidden="true">
          <rect x="4" y="1" width="8" height="14" rx="1.5" fill="none" stroke="#fbed22" stroke-width="1.6"/>
          <circle cx="8" cy="12.3" r="0.9" fill="#fbed22"/>
        </svg>
        <span>02 6911 5033</span>
      </li>
      <li>
        <svg class="contact-icon" viewBox="0 0 16 16" aria-hidden="true">
          <path d="M1 5.5 Q8 1 15 5.5 L13 7.5 L11 6 L11 4.8 Q8 4 5 4.8 L5 6 L3 7.5 Z" fill="#fbed22"/>
          <rect x="3" y="8.5" width="10" height="6" rx="1" fill="#fbed22"/>
        </svg>
        <span>0477 301 926</span>
      </li>
      <li>
        <svg class="contact-icon" viewBox="0 0 16 16" aria-hidden="true">
          <rect x="1" y="3" width="14" height="10" fill="#fbed22"/>
          <path d="M1 3 L8 9 L15 3" fill="none" stroke="#ffffff" stroke-width="1.3"/>
        </svg>
        <span>wombridgehire@tallnetmail.com</span>
      </li>
    </ul>

    <div class="accent-stripe"></div>
  </section>

</body>
</html>
```